Vantor Holdings - Brochure - Industrial Construction Services

We need a brochure design based on the power point presentation attached. Our business is named Vantor Holdings and is an industrial project services business concentrating on Construction Project Management, Technical Services, and Consulting. We want to communicate that "We offer our clients a
unique systematic approach to solving technical challenges." As you can see from our logo designs we like the colors blue and grey. We are after clean, but innovative design overall. We also seem to like design that have darker style backgrounds. We would like this brochure to be a bi-fold 8.5"x 5.5" size when closed if possible. If any files or graphics are needed in original format please request them. Thanks!

Target Market(s)

Large Oil & Gas, Power Generation, and Engineering Companies.

Industry/Entity Type

Engineering

Font styles to use
Serif

Requirements
Must have
• A strong-lasting first impression.

```html
<!DOCTYPE html>
<html lang="en">
<head>
<meta charset="utf-8">
<title>Vantor Holdings – Brochure Cover</title>
<link rel="stylesheet" href="https://fonts.googleapis.com/css2?family=Cinzel:wght@400;600&family=Arimo:wght@400;700&family=Oswald:wght@700&display=swap">
<style>
  :root {
    --page: #e4e6e8;
    --blue-deep: #0a5aa6;
    --blue-mid: #1b7fd0;
    --blue-light: #3a9ae4;
    --red: #e3202a;
    --red-dark: #c2161f;
    --grey-light: #f4f5f6;
    --grey-mid: #c9ccd0;
    --ink: #3b3f45;
    --white: #ffffff;
    --sky: #7fb2de;
    --plant: #9aa4ae;
  }
  * { box-sizing: border-box; margin: 0; padding: 0; }
  html, body { width: 1200px; height: 699px; overflow: hidden; background: var(--page); }
  .brochure {
    position: absolute; left: 40px; top: 163px;
    width: 1120px; height: 373px;
    display: flex;
    box-shadow: 0 4px 14px rgba(0,0,0,.18);
  }
  .panel { position: relative; width: 560px; height: 373px; overflow: hidden; }

  /* Back panel */
  .panel--contact {
    background: radial-gradient(ellipse at 65% 30%, var(--blue-light) 0%, var(--blue-mid) 40%, var(--blue-deep) 100%);
    color: var(--white);
    text-align: center;
  }
  .brand { position: absolute; left: 0; right: 0; }
  .brand__name {
    font-family: "Cinzel", serif; font-weight: 400;
    display: inline-flex; align-items: center; gap: 12px;
  }
  .brand__dot { width: 14px; height: 14px; border-radius: 50%; background: currentColor; display: inline-block; }
  .brand__tag { font-family: "Arimo", sans-serif; letter-spacing: 3px; text-transform: uppercase; }
  .panel--contact .brand { top: 138px; }
  .panel--contact .brand__name { font-size: 30px; }
  .panel--contact .brand__tag {
    font-size: 11.5px; margin-top: 4px; display: inline-block;
    border-top: 1px solid rgba(255,255,255,.8); padding-top: 3px;
  }
  .contact__title {
    position: absolute; top: 223px; left: 0; right: 0;
    font-family: "Arimo", sans-serif; font-size: 24px; font-weight: 400; letter-spacing: .5px;
  }
  .contact__rule { position: absolute; top: 270px; left: 133px; width: 294px; height: 1px; background: var(--white); }
  .contact__list { position: absolute; top: 285px; left: 0; right: 0; list-style: none;
    font-family: "Arimo", sans-serif; font-size: 14px; line-height: 19px; }

  .web-band {
    position: absolute; left: 0; bottom: 0; width: 100%; height: 39px;
    background: linear-gradient(180deg, var(--red) 0%, var(--red-dark) 100%);
    color: var(--white); font-family: "Arimo", sans-serif; font-size: 18px;
    letter-spacing: 12.5px; line-height: 39px; text-align: center; text-transform: uppercase;
  }

  /* Front panel */
  .panel--cover { background: linear-gradient(180deg, var(--white) 0%, var(--grey-light) 45%, var(--grey-mid) 100%); }
  .panel--cover .brand { left: 16px; right: auto; top: 68px; color: var(--ink); text-align: left; }
  .panel--cover .brand__name { font-size: 17px; gap: 7px; }
  .panel--cover .brand__dot { width: 9px; height: 9px; }
  .panel--cover .brand__tag { font-size: 6.5px; letter-spacing: 2.4px; display: block; margin-top: 2px; }
  .headline {
    position: absolute; top: 26px; right: 22px;
    font-family: "Oswald", sans-serif; font-weight: 700; font-size: 27px;
    color: var(--red); text-transform: uppercase; letter-spacing: .2px;
  }
  .cover-art { position: absolute; left: 0; top: 0; width: 560px; height: 373px; }
  .panel--cover .web-band { background: rgba(214,24,32,.82); }
</style>
</head>
<body>
  <div class="brochure">
    <section class="panel panel--contact">
      <div class="brand">
        <div class="brand__name"><span class="brand__dot"></span>Vantor Holdings</div><br>
        <span class="brand__tag">Management &amp; Consulting</span>
      </div>
      <h2 class="contact__title">CONTACT DETAILS</h2>
      <div class="contact__rule"></div>
      <ul class="contact__list">
        <li>0100-555-019</li>
        <li>info@vantorholdings.com</li>
      </ul>
      <div class="web-band">vantorholdings.com</div>
    </section>

    <section class="panel panel--cover">
      <svg class="cover-art" viewBox="0 0 560 373" xmlns="http://www.w3.org/2000/svg">
        <defs>
          <linearGradient id="siteTones" x1="0" y1="0" x2="0" y2="1">
            <stop offset="0" stop-color="var(--sky)"/>
            <stop offset="0.55" stop-color="var(--plant)"/>
            <stop offset="1" stop-color="#b4453c"/>
          </linearGradient>
        </defs>
        <path d="M14 373 Q110 60 560 138 L560 373 Z" fill="var(--blue-mid)"/>
        <path d="M24 373 Q120 76 560 153 L560 373 Z" fill="var(--white)"/>
        <path d="M30 373 Q126 84 560 160 L560 373 Z" fill="var(--red)"/>
        <path d="M40 373 Q136 98 560 174 L560 373 Z" fill="var(--white)"/>
        <path d="M45 373 Q141 104 560 180 L560 373 Z" fill="url(#siteTones)"
              role="img" aria-label="Photo of two engineers in hard hats and safety gear at an industrial refinery plant"/>
      </svg>
      <div class="brand">
        <div class="brand__name"><span class="brand__dot"></span>Vantor Holdings</div>
        <span class="brand__tag">Management &amp; Consulting</span>
      </div>
      <h1 class="headline">Knowledge Integrity Quality</h1>
      <div class="web-band">vantorholdings.com</div>
    </section>
  </div>
</body>
</html>
```